Health Coaching Brochure for Healthcare Practioners

I am looking to have a tri-fold brochure created marketed towards healthcare practitioners (doctors, nurses, surgeons, etc), to get them to purchase 1-on-1 health coaching from me.
I've provided the text/content (in pdf & pages), my logo, a picture of me, and two color palettes, but please also include lots of white space. I would like to design to be very clean, modern & crisp. Also include additional photos, of doctors, etc taking care of themselves & feeling happy (maybe eating healthy, maybe exercising, feeling good & happy!)
Please also see http://tallbirchwellness.com and http://instagram.com/tallbirchwellness for a feel of my brand.
Thank you!
Target Market(s)
Healthcare Practioners (mainly based in Los Angeles, for now)
Industry/Entity Type
Healthcare
Look and feel
Each slider illustrates characteristics of the customer's brand and the style your logo design should communicate.

```html
<!DOCTYPE html>
<html lang="en">
<head>
<meta charset="utf-8">
<title>Tall Birch Wellness – Tri-fold Brochure</title>
<link rel="stylesheet" href="https://fonts.googleapis.com/css2?family=Open+Sans:wght@300;400;600;700&family=Ubuntu:wght@500;700&family=Roboto+Condensed:ital,wght@0,700;1,700&display=swap">
<style>
  :root{
    --sheet:#262626;
    --sky:#2a9bd6;
    --teal:#1bb0c3;
    --deep:#2c7cb5;
    --gold:#b27e2e;
    --sand:#e5c39f;
    --ink:#1e1e1e;
    --paper:#ffffff;
    --accent:#2193c6;
  }
  *{box-sizing:border-box;margin:0;padding:0}
  html,body{width:776px;height:1200px;overflow:hidden;background:var(--sheet)}
  body{font-family:"Open Sans",Arial,sans-serif;color:var(--paper)}
  .canvas{position:relative;width:776px;height:1200px}
  .abs{position:absolute}
  .label{font-family:"Open Sans",Arial,sans-serif;font-weight:700;font-size:13px;color:var(--paper)}
  .fold{position:absolute;border-left:1px dashed #777}
  .panel{position:absolute;overflow:hidden}
  .panel svg{position:absolute;left:0;top:0}
  .photo{position:absolute}
  .heading{font-family:"Ubuntu",sans-serif;font-weight:700}
  .small{font-size:6.4px;line-height:9.4px;text-align:justify}
  .cond{font-family:"Roboto Condensed",sans-serif;font-weight:700}
  .brand{font-family:"Open Sans",sans-serif;font-weight:700;color:var(--ink);font-size:16px}
  .training{font-family:"Open Sans",sans-serif;font-weight:700;font-style:italic;color:var(--ink);font-size:14px}
  .place{font-size:8.5px;color:var(--ink)}
  .feature-list{list-style:none}
  .feature-list li{position:relative;padding-left:9px;font-size:6.8px;line-height:12px;color:var(--ink)}
  .feature-list li::before{content:"";position:absolute;left:0;top:4px;width:5px;height:5px;border-radius:50%;background:var(--gold)}
  .dark{color:var(--ink)}
  .about-copy{position:absolute;left:14px;top:22px;width:201px}
  .about-copy .portrait{float:right;width:58px;height:58px;margin:0 0 4px 6px;border-radius:50%;border:2px solid #fff;background:radial-gradient(circle at 50% 45%,#e8c9b5,#4a2e24 75%)}
  .about-copy h2{font-size:22px;line-height:26px;margin-bottom:10px}
  .about-copy p + p{margin-top:8px}
  .testimonial-copy{position:absolute;left:20px;top:267px;width:190px}
  .testimonial-copy h2{font-weight:300;font-size:14px;letter-spacing:.3px;margin-bottom:6px}
  .testimonial-copy p + p{margin-top:10px}
  .testimonial-copy .author{text-align:right;font-size:7.5px;margin-top:8px;margin-bottom:14px}
</style>
</head>
<body>
<div class="canvas">

  <div class="abs label" style="left:49px;top:27px">Back side Left</div>
  <div class="abs label" style="left:341px;top:27px">Back side</div>
  <div class="abs label" style="left:656px;top:27px">Front Side</div>
  <div class="abs label" style="left:49px;top:1155px">Inside Left</div>
  <div class="abs label" style="left:341px;top:1155px">Inside Middle</div>
  <div class="abs label" style="left:656px;top:1155px">Inside Right</div>
  <div class="fold" style="left:274px;top:40px;height:1120px"></div>
  <div class="fold" style="left:501px;top:40px;height:1120px"></div>

  <!-- Outside: testimonials panel -->
  <section class="panel testimonials" style="left:46px;top:55px;width:228px;height:531px;background:var(--sky)">
    <svg width="228" height="531" viewBox="0 0 228 531">
      <polygon points="0,205 228,250 228,275 0,222" fill="var(--gold)"/>
    </svg>
    <div class="photo" role="img" aria-label="Healthy salad plate" style="left:0;top:0;width:94px;height:129px;background:linear-gradient(135deg,#e8e2d6,#c9563a 60%,#6d8a3c)"></div>
    <div class="photo" role="img" aria-label="Meal prep containers with vegetables and chicken" style="left:96px;top:0;width:132px;height:129px;background:linear-gradient(135deg,#dcd7cf,#4f6b33 45%,#7a4a2a)"></div>
    <div class="photo" role="img" aria-label="Salmon with squash blossoms" style="left:0;top:131px;width:115px;height:95px;background:linear-gradient(135deg,#c36a3a,#e3a153 50%,#6f8f3a);clip-path:polygon(0 0,100% 0,100% 100%,0 78%)"></div>
    <div class="photo" role="img" aria-label="Woman drinking a fresh orange juice" style="left:117px;top:131px;width:111px;height:115px;background:linear-gradient(135deg,#e9e3dc,#e0722c 55%,#b5532a);clip-path:polygon(0 0,100% 0,100% 100%,0 82%)"></div>

    <div class="testimonial-copy">
      <h2>TESTIMONIALS</h2>
      <p class="small">Maya is the perfect balance of tough and caring. She has this way of making me feel like I can push myself without being too stern.</p>
      <p class="small">I love how every session she mixes up the exercises so that they are varied, and never get boring. She is super professional, motivating, knowledgeable and a pleasure to be around. I have been working with her 3X/week for just over a month and I have lost inches off my waist and butt, and lost eight pounds. Prior to working with Maya I was super sedentary and since having a baby last year, I also just haven't felt good in my body. Maya has made me feel motivated and strong and after every session with her I feel confident that I can reach my goals and feel healthy and active again.</p>
      <p class="author">Jolene Carter</p>
      <p class="small">She's helped me transform myself from an overweight junk food eater to a much fitter and healthier person. I highly recommend Maya to anyone and everyone.</p>
      <p class="author">Rosa Whitfield</p>
    </div>
  </section>

  <!-- Outside: about panel -->
  <section class="panel about" style="left:274px;top:55px;width:228px;height:531px;background:var(--teal)">
    <div class="about-copy">
      <div class="portrait" role="img" aria-label="Portrait of the coach"></div>
      <h2 class="heading">About Me</h2>
      <p class="small">Maya Lindqvist is a personal trainer, fitness nutritionist, and holistic health coach based in Los Angeles, California. Maya helps clients improve their health, develop sustainable habits, and achieve their goals to be their best, most vibrant selves.</p>
      <p class="small">Maya sought fitness in 2005 to overcome her lifelong battle of depression, anxiety, and an extra 30 pounds. After completely transforming her body and her mind, she realized that transformation spilling over to other areas of her life – career, relationships, and self-worth. She began to help other people transform their lives, as well.</p>
      <p class="small">Fitness was only the beginning. Maya's journey has continued to evolve to include a more holistic approach. While getting clients the bodies they want, she puts an even stronger emphasis on health and longevity. She believes proper and efficient digestion is the key to not only getting the body they want, but also to preventing all diseases.</p>
    </div>
    <div class="abs" style="left:14px;top:253px;width:195px;height:98px;border-radius:10px;background:var(--sand);color:var(--ink);font-size:24px;display:flex;align-items:center;justify-content:center">map</div>
    <p class="abs" style="left:10px;top:361px;width:208px;text-align:center;font-size:7px;line-height:11px">Personal training sessions are held in a private studio in Glendale, CA or at your home.</p>
    <p class="abs" style="left:0;top:395px;width:228px;text-align:center;font-size:16px">MAYA LINDQVIST</p>
    <p class="abs" style="left:0;top:416px;width:228px;text-align:center;font-size:6.6px;font-weight:600">Holistic Nutrition &amp; Health Coach and Personal Trainer</p>
    <p class="abs" style="left:0;top:430px;width:228px;text-align:center;font-size:7px;letter-spacing:.6px">maya@tallbirchwellness.com</p>
    <p class="abs heading" style="left:0;top:457px;width:228px;text-align:center;font-size:14px;line-height:16px;font-weight:500">CALL FOR A FREE 15<br>MINUTE CONSULTATION</p>
    <p class="abs cond" style="left:0;top:490px;width:228px;text-align:center;font-size:20px;font-weight:400">000 0000 0000</p>
  </section>

  <!-- Outside: cover panel -->
  <section class="panel cover" style="left:502px;top:55px;width:230px;height:531px;background:var(--paper)">
    <svg width="230" height="531" viewBox="0 0 230 531">
      <polygon points="0,61 230,145 0,85" fill="var(--gold)"/>
      <polygon points="0,355 230,380 230,437" fill="var(--gold)"/>
      <polygon points="0,355 230,437 230,531 0,531" fill="var(--sky)"/>
    </svg>
    <div class="photo" role="img" aria-label="Woman jumping joyfully on the beach" style="left:0;top:0;width:230px;height:531px;background:linear-gradient(180deg,#d9dde0 0%,#9fb0bd 45%,#5c6f7e 70%,#c7c2b7 100%);clip-path:polygon(0 85px,230px 145px,230px 380px,0 355px)"></div>
    <p class="abs brand" style="right:20px;top:22px">Tall Birch Wellness</p>
    <p class="abs training" style="right:22px;top:52px;text-align:right;line-height:17px">1-on-1<br>Personal Training</p>
    <p class="abs place" style="right:22px;top:89px">Los Angeles, CA</p>
    <div class="abs heading" style="left:21px;top:400px;font-size:17px;line-height:23.2px;font-weight:500">
      Get In Shape<br>Lose Weight<br>Tone Up<br>Look &amp; Feel Better<br>Than Ever
    </div>
  </section>

  <!-- Inside: photo strip and banner -->
  <section class="panel inside" style="left:46px;top:610px;width:686px;height:532px;background:var(--paper)">
    <div class="photo" role="img" aria-label="Chocolate protein bars" style="left:0;top:0;width:124px;height:168px;background:linear-gradient(135deg,#f0ece8,#4a2c1e 55%,#c9a477)"></div>
    <div class="photo" role="img" aria-label="Green smoothie bowl with granola" style="left:128px;top:0;width:144px;height:168px;background:linear-gradient(135deg,#8a5a2e,#b07a3e 45%,#6ea04c)"></div>
    <div class="photo" role="img" aria-label="Colourful prepared meals and fruit" style="left:275px;top:0;width:165px;height:168px;background:linear-gradient(135deg,#5a6b3a,#e39b3f 40%,#c63d3a 70%,#3e3e2e)"></div>
    <div class="photo" role="img" aria-label="Chocolate smoothie in a jar" style="left:443px;top:0;width:120px;height:168px;background:linear-gradient(180deg,#f4f1ee,#7a5140 45%,#9c7363)"></div>
    <div class="photo" role="img" aria-label="Green juice in a glass" style="left:566px;top:0;width:120px;height:168px;background:linear-gradient(180deg,#f6f6f2,#5f8e2c 55%,#3d6b1c)"></div>

    <div class="abs" style="left:0;top:168px;width:686px;height:82px;background:var(--teal)"></div>
    <div class="abs" style="left:0;top:250px;width:686px;height:14px;background:var(--deep)"></div>

    <div class="abs cond" style="left:22px;top:177px;font-size:15.5px;line-height:23px;font-style:italic">
      ARE YOU FEELING… Overwhelmed? Exhausted?<br>Struggling with food and feeling guilty about it?<br><span style="display:inline-block;margin-top:2px">Like you know what you SHOULD do but aren't doing it?</span>
    </div>
    <p class="abs heading" style="left:469px;top:178px;font-size:13.5px;line-height:15.5px;font-weight:500">CALL FOR A FREE 15<br>MINUTE CONSULTATION</p>
    <p class="abs cond" style="left:469px;top:212px;font-size:23px;font-weight:400">000 0000 0000</p>

    <svg width="686" height="532" viewBox="0 0 686 532" style="top:0">
      <path d="M456,422 Q570,368 686,420 L686,532 L456,532 Z" fill="var(--teal)"/>
      <path d="M456,426 Q570,375 686,426 L686,532 L456,532 Z" fill="var(--gold)"/>
    </svg>
  </section>

  <!-- inside left -->
  <div class="abs dark" style="left:66px;top:882px;width:200px">
    <p style="font-size:8px;line-height:11px;font-weight:600">Get the most out of your workout by working out with a personal trainer</p>
    <ul class="feature-list" style="margin-top:3px">
      <li style="line-height:9.5px">Customized workout program, from beginner to advanced</li>
      <li>Provide motivation, support, and accountability</li>
    </ul>
    <p style="font-size:8px;font-weight:600;margin-top:4px;margin-bottom:2px">Achieve your fitness goals and have fun doing it</p>
    <ul class="feature-list">
      <li>Fat Loss</li>
      <li>Weight Training</li>
      <li>Cardiovascular Training</li>
      <li>Muscular Development &amp; Toning</li>
      <li>Sports Performance Training</li>
      <li>Body Composition Analysis</li>
      <li>Specialized Diet Plans</li>
      <li>Nutrition &amp; Supplementation Counseling</li>
      <li>Wedding Preparation</li>
    </ul>
    <p style="font-size:8px;line-height:11px;font-weight:600;margin-top:6px">Integrative Nutrition &amp; Health Coaching available, as well.</p>
    <p style="font-size:8px;font-weight:600;margin-top:7px">+24-hour access to trainer</p>
  </div>

  <!-- inside middle -->
  <div class="abs" style="left:274px;top:879px;width:228px;text-align:center;color:var(--accent)">
    <h2 class="heading" style="font-size:19px;font-weight:500">Function movements!</h2>
    <p class="heading" style="font-size:15.5px;line-height:20.5px;font-weight:500;margin-top:9px">Based on how your body<br>was designed to move<br>ready to make the<br>commitment?</p>
    <p class="heading" style="font-size:15.5px;line-height:20.5px;font-weight:500;margin-top:9px">schedule your 15 minute<br>consultation today!</p>
    <p class="brand" style="margin-top:17px">Tall Birch Wellness</p>
    <p class="training" style="margin-top:6px">1-on-1 Personal Training</p>
    <p class="place">Los Angeles, CA</p>
  </div>

  <!-- inside right -->
  <div class="abs dark" style="left:514px;top:886px;width:193px">
    <p class="small" style="font-size:6.7px;line-height:10.7px">Helping others is my passion. Seeing the change in someone throughout their fitness journey is incredible. Not just physically, but also emotionally. They have become more confident, more optimistic, healthier and stronger in all aspects of their life.</p>
    <p class="small" style="font-size:6.7px;line-height:10.7px;margin-top:6px">Working with all different skill sets and fitness levels I am always working for my clients. Doing everything I can to teach them how to live a healthier life.</p>
    <p style="font-size:6.7px;margin-top:8px">let's do it together!</p>
  </div>
  <div class="abs" style="left:502px;top:1012px;width:230px;text-align:center">
    <p class="heading" style="font-size:13px;line-height:14px;font-weight:500">HOW WOULD IT<br>FEEL TO</p>
    <p style="font-size:9.6px;line-height:13.5px;font-weight:600;margin-top:8px">Wake up feeling light and energized?</p>
    <p style="font-size:9.6px;line-height:13.5px;font-weight:600;margin-top:3px">Finally get a handle on food and your<br>cravings?</p>
    <p style="font-size:9.6px;line-height:13.5px;font-weight:600;margin-top:3px">Reach all of your health goals and life<br>goals?</p>
  </div>

</div>
</body>
</html>
```